Postcard Design

We offer facilitated group glasses in senior living facilities centered around memoir and life story writing. The postcards will go to administrators, activity directors and program directors at facilities, and potentially to librarians, staff and senior centers etc... So we want to say a little bit about WHY life writing is important to this population. I will upload a flyer I made myself. This will give you a sense of what we do and what we are trying to impart.
I've been using bright colors because they appeal to our population - blue is critical (Tinfern Story Circle) and I'm down with anything else.
I have several images from google images that I've been using, but I'm not particularly attached to them. I did buy the rights to the blue owl guy and I have it in several formats and sizes.

I'm also including a power point that describes our course work, though I don't expect you to read it! Just trying to include anything that might be helpful. Any suggestions are most welcome!!! Thanks!

Industry/Entity Type

Group

```html
<!DOCTYPE html>
<html lang="en">
<head>
<meta charset="utf-8">
<title>Tinfern Story Circle – Postcard</title>
<link rel="stylesheet" href="https://fonts.googleapis.com/css2?family=Lato:ital,wght@0,400;0,700;1,400&family=Oswald:wght@500&family=PT+Serif:wght@400;700&display=swap">
<style>
  :root {
    --stage: #3b3b3b;
    --paper: #ffffff;
    --sky: #39aee3;
    --sky-deep: #1f8fcb;
    --teal: #1f7d6c;
    --pink: #e51f7c;
    --pink-light: #f25aa0;
    --orange: #f4a21f;
    --grey-band: #8b8c8f;
    --ink: #333333;
    --white: #ffffff;
  }
  * { box-sizing: border-box; margin: 0; padding: 0; }
  html, body { width: 900px; height: 1200px; overflow: hidden; }
  body { background: var(--stage); font-family: "Lato", sans-serif; position: relative; }

  .card { position: absolute; background: var(--paper); overflow: hidden; }
  .card svg.card-art { position: absolute; inset: 0; }
  .card-front { left: 92px; top: 75px; width: 716px; height: 465px; }
  .card-back { left: 95px; top: 632px; width: 695px; height: 468px; }

  .brand { position: absolute; display: flex; flex-direction: column; align-items: center; gap: 8px; }
  .brand-dot { width: 46px; height: 46px; border-radius: 50%; background: var(--sky); }
  .brand-name { font-family: "Lato", sans-serif; font-weight: 700; font-size: 14px; color: var(--sky-deep); white-space: nowrap; }
  .card-front .brand { left: 18px; top: 26px; }
  .card-back .brand { left: 176px; top: 22px; }

  .headline { position: absolute; left: 283px; top: 56px; font-family: "PT Serif", serif; }
  .headline-main { font-size: 19px; color: var(--pink); }
  .headline-sub { font-size: 15.5px; color: var(--ink); margin-top: 1px; }

  .placeholder { position: absolute; }
  .book-art { background: linear-gradient(90deg, #e8433a, #f4c21f 30%, #3cb54a 55%, #2f8fd8 75%, #8e44ad); border-radius: 3px 3px 10px 10px; }
  .card-front .book-art { left: 563px; top: 40px; width: 92px; height: 62px; }
  .card-back .book-art { left: 523px; top: 48px; width: 70px; height: 40px; }
  .flower { border-radius: 50%; background: radial-gradient(circle, rgba(240,106,168,0.75) 0%, rgba(240,106,168,0.35) 55%, rgba(240,106,168,0) 72%); }

  .pill { position: absolute; left: 140px; top: 155px; width: 132px; height: 30px; border-radius: 15px; background: linear-gradient(var(--pink-light), var(--pink)); border: 2px solid var(--white); color: var(--white); font-family: "Oswald", sans-serif; font-size: 17px; text-align: center; line-height: 25px; }

  .about-copy { position: absolute; left: 41px; top: 198px; width: 345px; color: var(--white); font-size: 10.2px; line-height: 12.6px; text-align: justify; }
  .about-copy p + p { margin-top: 8px; }

  .contact { position: absolute; color: var(--white); font-size: 11.5px; font-weight: 700; line-height: 15px; }
  .contact li { list-style: none; display: flex; align-items: center; gap: 6px; }
  .contact svg { flex: none; }
  .card-front .contact-left { left: 24px; top: 414px; }
  .card-front .contact-right { left: 246px; top: 414px; }
  .card-back .contact { left: 16px; top: 372px; font-size: 11.5px; line-height: 14.5px; }

  .tag { position: absolute; left: 0; height: 20px; padding: 0 24px 0 12px; background: var(--orange); color: var(--ink); font-size: 13px; line-height: 20px; clip-path: polygon(0 0, calc(100% - 12px) 0, 100% 50%, calc(100% - 12px) 100%, 0 100%); }
  .tag-facilitator { top: 151px; }
  .tag-testimonial { top: 256px; }

  .facilitator-copy { position: absolute; left: 20px; top: 180px; width: 380px; color: var(--white); font-size: 10.2px; line-height: 12.4px; text-align: justify; }
  .testimonial { position: absolute; left: 20px; top: 282px; width: 312px; color: var(--white); font-size: 10.2px; line-height: 12.4px; font-style: italic; text-align: justify; }
  .testimonial cite { display: block; text-align: right; margin-right: 24px; color: var(--orange); font-weight: 700; font-size: 10px; }

  .stamp-box { position: absolute; left: 625px; top: 45px; width: 48px; height: 48px; border: 1.5px solid var(--ink); }
  .address-line { position: absolute; left: 500px; width: 165px; border-top: 1.5px solid var(--ink); }
</style>
</head>
<body>

<section class="card card-front" aria-label="Postcard front">
  <svg class="card-art" viewBox="0 0 716 465" width="716" height="465" aria-hidden="true">
    <defs>
      <linearGradient id="front-paper" x1="0" y1="0" x2="0" y2="1">
        <stop offset="0" stop-color="#ffffff"/><stop offset="1" stop-color="#e6e6e7"/>
      </linearGradient>
      <linearGradient id="front-sky" x1="0" y1="0" x2="0" y2="1">
        <stop offset="0" stop-color="#6cc8ee"/><stop offset="1" stop-color="#2b9bd4"/>
      </linearGradient>
      <linearGradient id="front-photo" x1="0" y1="0" x2="1" y2="1">
        <stop offset="0" stop-color="#d8d2c9"/><stop offset="0.5" stop-color="#c9ad97"/><stop offset="1" stop-color="#8aa6c4"/>
      </linearGradient>
    </defs>
    <rect width="716" height="465" fill="url(#front-paper)"/>
    <rect y="385" width="716" height="80" fill="#8b8c8f"/>
    <path d="M0 160 C130 138 270 128 415 150 L422 382 C300 396 150 378 0 392 Z" fill="url(#front-sky)"/>
    <path d="M0 160 C130 138 270 128 415 150" fill="none" stroke="#f4a21f" stroke-width="5"/>
    <path d="M0 394 C150 380 300 398 422 384" fill="none" stroke="#f4a21f" stroke-width="6"/>
    <path d="M0 186 C120 160 260 140 400 150 C520 160 620 150 716 150" fill="none" stroke="#1f7d6c" stroke-width="9"/>
    <path d="M240 0 C210 70 120 120 0 150" fill="none" stroke="#1f7d6c" stroke-width="5"/>
    <path d="M418 172 C520 158 620 154 716 162 L716 465 L650 465 C520 430 440 330 418 172 Z" fill="url(#front-photo)"/>
    <path d="M414 172 C438 330 520 430 650 462" fill="none" stroke="#e51f7c" stroke-width="9"/>
  </svg>

  <div class="brand">
    <span class="brand-dot"></span>
    <span class="brand-name">Tinfern Story Circle</span>
  </div>

  <div class="headline">
    <div class="headline-main">Life Story Writing For Seniors</div>
    <div class="headline-sub">8 Sessions with Follow-on Facilitation</div>
  </div>

  <div class="placeholder book-art" role="img" aria-label="Illustration of an open book with rainbow pages"></div>
  <div class="placeholder" role="img" aria-label="Photo of four seniors smiling around a laptop" style="left:470px;top:200px;width:230px;height:220px;"></div>
  <div class="placeholder flower" role="img" aria-label="Decorative flower cluster" style="left:644px;top:108px;width:52px;height:52px;"></div>
  <div class="placeholder flower" role="img" aria-label="Decorative flower cluster" style="left:360px;top:365px;width:80px;height:80px;"></div>
  <div class="placeholder flower" role="img" aria-label="Decorative flower" style="left:14px;top:146px;width:34px;height:34px;"></div>

  <div class="pill">About Us</div>

  <div class="about-copy">
    <p>The markers of a life well lived are the stories told, retold, and re-experienced. Life story writing captures the priceless and the poignant, the truly memorable and the quirkily remembered, the historic and the unique. It leaves a legacy of living history for future generations and brings enjoyment, satisfaction and closure to the author.</p>
    <p>Life writing classes decrease isolation, reawaken dormant interests, offer purposeful activity and hone cognitive skills. Your residents will love writing in a structured, facilitated group, hearing the stories of others, and experiencing the power of writing and sharing one's own story with a listening audience.</p>
    <p>Seniors learn to see themselves as part of a historical landscape that spans an entire century – and they are frequently awed at the way their individual lives have intersected...and mattered.</p>
  </div>

  <ul class="contact contact-left">
    <li><svg width="9" height="11" viewBox="0 0 9 11"><path d="M4.5 0A4 4 0 0 0 .5 4c0 3 4 7 4 7s4-4 4-7a4 4 0 0 0-4-4z" fill="#f4a21f"/><circle cx="4.5" cy="4" r="1.5" fill="#8b8c8f"/></svg>Tinfern Story Circle&nbsp; Ruth Calloway</li>
    <li><svg width="9" height="9" viewBox="0 0 10 10"><path d="M2 0l2 2.5-1.2 1.3a6 6 0 0 0 3.4 3.4L7.5 6 10 8l-1.5 2A8.5 8.5 0 0 1 0 1.5z" fill="#f4a21f"/></svg>555-014-2290</li>
  </ul>
  <ul class="contact contact-right">
    <li><svg width="10" height="7" viewBox="0 0 10 7"><rect width="10" height="7" rx="1" fill="#f4a21f"/></svg>ruth@tinfernstory.biz</li>
    <li><svg width="10" height="10" viewBox="0 0 10 10"><circle cx="5" cy="5" r="4.3" fill="none" stroke="#f4a21f" stroke-width="1.4"/></svg>www.tinfernstory.biz</li>
  </ul>
</section>

<section class="card card-back" aria-label="Postcard back">
  <svg class="card-art" viewBox="0 0 695 468" width="695" height="468" aria-hidden="true">
    <defs>
      <linearGradient id="back-paper" x1="0" y1="0" x2="0" y2="1">
        <stop offset="0" stop-color="#ffffff"/><stop offset="1" stop-color="#ececec"/>
      </linearGradient>
      <linearGradient id="back-sky" x1="0" y1="0" x2="1" y2="0">
        <stop offset="0" stop-color="#2b9bd4"/><stop offset="1" stop-color="#8fd6f4"/>
      </linearGradient>
      <linearGradient id="back-photo" x1="0" y1="0" x2="1" y2="1">
        <stop offset="0" stop-color="#e2d6c8"/><stop offset="0.6" stop-color="#cfae95"/><stop offset="1" stop-color="#9fb7cf"/>
      </linearGradient>
    </defs>
    <path d="M0 0 H440 C430 60 300 130 0 150 Z" fill="url(#back-paper)"/>
    <rect width="182" height="148" fill="url(#back-photo)"/>
    <path d="M0 148 C180 152 370 122 432 10 C470 120 445 280 335 400 L0 400 Z" fill="#1f7d6c"/>
    <path d="M0 148 C180 152 370 122 432 10" fill="none" stroke="#e51f7c" stroke-width="5"/>
    <path d="M0 342 C120 336 250 346 372 388 C340 420 310 445 286 468 L0 468 Z" fill="url(#back-sky)"/>
    <path d="M446 6 C488 130 462 300 318 468" fill="none" stroke="#f4a21f" stroke-width="14"/>
    <path d="M470 0 C514 150 486 320 348 468" fill="none" stroke="#e51f7c" stroke-width="14"/>
  </svg>

  <div class="placeholder" role="img" aria-label="Photo of four smiling seniors posing together" style="left:0;top:0;width:182px;height:148px;"></div>

  <div class="brand">
    <span class="brand-dot"></span>
    <span class="brand-name">Tinfern Story Circle</span>
  </div>

  <div class="placeholder flower" role="img" aria-label="Decorative flower cluster" style="left:392px;top:16px;width:78px;height:78px;"></div>
  <div class="placeholder flower" role="img" aria-label="Decorative flower cluster" style="left:342px;top:104px;width:52px;height:52px;"></div>
  <div class="placeholder flower" role="img" aria-label="Decorative flower cluster" style="left:184px;top:338px;width:78px;height:78px;"></div>

  <div class="tag tag-facilitator">About the facilitator:</div>
  <p class="facilitator-copy">Ruth Calloway has spent more than 25 years working with seniors in a variety of settings, including 18 years as the Executive Director of the Movement Wellness Alliance of the Plains where she also designed programs and services. She has published several short stories and is currently working on a fictionalized account of her grandmother's life, with an advance from a major publisher.</p>

  <div class="tag tag-testimonial">Testimonial</div>
  <blockquote class="testimonial">"This was my favorite experience of the last several years. I learned about myself and had such fun remembering the good times in my life. My children are thrilled with my writing! Ruth was so kind and patient and helpful. This was really a wonderful class!"
    <cite>Marian, 79</cite>
  </blockquote>

  <ul class="contact">
    <li><svg width="9" height="9" viewBox="0 0 10 10"><path d="M2 0l2 2.5-1.2 1.3a6 6 0 0 0 3.4 3.4L7.5 6 10 8l-1.5 2A8.5 8.5 0 0 1 0 1.5z" fill="#fff"/></svg>555-014-2290</li>
    <li><svg width="10" height="7" viewBox="0 0 10 7"><rect width="10" height="7" rx="1" fill="#fff"/></svg>ruth@tinfernstory.biz</li>
    <li><svg width="10" height="10" viewBox="0 0 10 10"><circle cx="5" cy="5" r="4.3" fill="none" stroke="#fff" stroke-width="1.4"/></svg>www.tinfernstory.biz</li>
    <li><svg width="9" height="11" viewBox="0 0 9 11"><path d="M4.5 0A4 4 0 0 0 .5 4c0 3 4 7 4 7s4-4 4-7a4 4 0 0 0-4-4z" fill="#fff"/><circle cx="4.5" cy="4" r="1.5" fill="#2b9bd4"/></svg>Tinfern Story Circle</li>
    <li style="padding-left:15px;">Ruth Calloway</li>
  </ul>

  <div class="placeholder book-art" role="img" aria-label="Illustration of an open book with rainbow pages"></div>
  <div class="stamp-box" aria-label="Stamp area"></div>
  <div class="address-line" style="top:283px;"></div>
  <div class="address-line" style="top:306px;"></div>
  <div class="address-line" style="top:330px;"></div>
</section>

</body>
</html>
```